Poster to display corporate values and behaviors associated

I'm looking for a graphic design, probably in the form of a poster or something that can be posted on walls throughout the building that identifies our "Brightwell Values".
The values are: Accountability, Honesty, Excellence, Teamwork, and Family.
Associated behaviors (which I'd like displayed with each value) are:
Accountability: Integrity, Trust, Self-Discipline, Tranparency
Honesty: Integrity, Pschological Safety, Vulnerability, Dependable, Ethical, Truthful
Excellence: Consistent Quality, Continuous Improvement, Attention to Detail, Accepting Challenges, Service to others (internally and externally)
Teamwork: Acknowledging strengths and weaknesses, Compromise, Active listening, Punctuality, Open to Feedback, Mutual Respect
Family: Acceptance, Compassion, Being there for each other, Celebrating Successes
I have attached an example that my team put together, however it is too small for something on the wall, and am looking for other options.
Feel free to use our corporate logo as well (attached)

```html
<!DOCTYPE html>
<html lang="en">
<head>
<meta charset="utf-8">
<title>Brightwell Values</title>
<link href="https://fonts.googleapis.com/css2?family=Oswald:wght@700&family=Roboto+Condensed:wght@400;700&display=swap" rel="stylesheet">
<style>
  :root {
    --bg: #d3cfcd;
    --ink: #0b0b0b;
    --red: #e3302f;
    --red-dark: #6e0808;
    --grey-band: #666666;
    --grey-light: #b0b0b4;
    --grey-dark: #55565a;
    --ring: #e4e1df;
    --white: #ffffff;
    --divider: #c9c6c4;
  }
  * { margin: 0; padding: 0; box-sizing: border-box; }
  html, body { width: 1200px; height: 727px; overflow: hidden; background: var(--bg); }
  .poster {
    position: relative; width: 1200px; height: 727px; overflow: hidden;
    background: linear-gradient(180deg, #d8d4d2 0%, #cfcbc9 60%, #b9b5b3 100%);
    font-family: "Roboto Condensed", "Arial Narrow", sans-serif;
  }
  .art { position: absolute; inset: 0; }
  .value-label {
    position: absolute; right: 458px; width: 320px; text-align: right;
    font-family: "Oswald", "Arial Narrow", sans-serif; font-weight: 700;
    font-size: 30px; letter-spacing: -0.5px; color: var(--white);
    line-height: 1; transform: translateY(-50%);
  }
  .behaviours {
    position: absolute; left: 770px; width: 430px; display: flex;
    padding: 14px 0 0 20px; font-size: 16.5px; color: var(--ink); line-height: 20.5px;
  }
  .behaviours ul { list-style: none; }
  .behaviours li { position: relative; padding-left: 13px; }
  .behaviours li::before {
    content: ""; position: absolute; left: 0; top: 7px; width: 6px; height: 6px;
    border-radius: 50%; background: var(--red);
  }
  .col-wide { width: 216px; }
  .col-mid { width: 124px; }
  .brand-name {
    position: absolute; left: 173px; top: 364px; transform: translate(-50%, -50%);
    font-family: "Roboto Condensed", "Arial Narrow", sans-serif; font-weight: 700;
    font-size: 21px; color: var(--white);
  }
</style>
</head>
<body>
<main class="poster">
  <svg class="art" width="1200" height="727" viewBox="0 0 1200 727" xmlns="http://www.w3.org/2000/svg">
    <defs>
      <linearGradient id="band-red" x1="450" y1="0" x2="770" y2="0" gradientUnits="userSpaceOnUse">
        <stop offset="0" stop-color="#6e0808"/><stop offset="1" stop-color="#e3302f"/>
      </linearGradient>
      <linearGradient id="band-grey" x1="509" y1="0" x2="770" y2="0" gradientUnits="userSpaceOnUse">
        <stop offset="0" stop-color="#55565a"/><stop offset="1" stop-color="#b0b0b4"/>
      </linearGradient>
      <radialGradient id="ring-fill" cx="173" cy="364" r="341" gradientUnits="userSpaceOnUse">
        <stop offset="0.82" stop-color="#b9b6b4"/><stop offset="0.9" stop-color="#e9e7e6"/><stop offset="1" stop-color="#dcd9d7"/>
      </radialGradient>
      <radialGradient id="hub-fill" cx="200" cy="340" r="130" gradientUnits="userSpaceOnUse">
        <stop offset="0" stop-color="#f2f2f2"/><stop offset="1" stop-color="#8e8e8e"/>
      </radialGradient>
      <clipPath id="right-half"><rect x="177" y="0" width="1023" height="727"/></clipPath>
    </defs>

    <rect class="hub-band" x="0" y="251" width="180" height="225" fill="var(--grey-band)"/>

    <g class="value-bands">
      <rect x="190" y="25" width="580" height="114" fill="var(--ink)"/>
      <rect x="300" y="167" width="470" height="113" fill="url(#band-red)"/>
      <rect x="300" y="307" width="470" height="113" fill="url(#band-grey)"/>
      <rect x="300" y="447" width="470" height="113" fill="url(#band-red)"/>
      <rect x="176" y="588" width="594" height="113" fill="var(--ink)"/>
    </g>

    <g class="behaviour-boxes">
      <rect x="770" y="25" width="430" height="114" fill="var(--white)"/>
      <rect x="770" y="25" width="430" height="2" fill="var(--ink)"/><rect x="770" y="137" width="430" height="2" fill="var(--ink)"/>
      <rect x="770" y="167" width="430" height="113" fill="var(--white)"/>
      <rect x="770" y="167" width="430" height="2" fill="var(--red)"/><rect x="770" y="278" width="430" height="2" fill="var(--red)"/>
      <rect x="770" y="307" width="430" height="113" fill="var(--white)"/>
      <rect x="770" y="307" width="430" height="2" fill="var(--grey-light)"/><rect x="770" y="418" width="430" height="2" fill="var(--grey-light)"/>
      <rect x="770" y="447" width="430" height="113" fill="var(--white)"/>
      <rect x="770" y="447" width="430" height="2" fill="var(--red)"/><rect x="770" y="558" width="430" height="2" fill="var(--red)"/>
      <rect x="770" y="588" width="430" height="113" fill="var(--white)"/>
      <rect x="770" y="588" width="430" height="2" fill="var(--ink)"/><rect x="770" y="699" width="430" height="2" fill="var(--ink)"/>
    </g>

    <g class="wheel" clip-path="url(#right-half)">
      <circle class="outer-ring" cx="173" cy="364" r="341" fill="url(#ring-fill)"/>
      <circle class="sector-face" cx="173" cy="364" r="285" fill="var(--white)" stroke="#c4c1bf" stroke-width="3"/>
      <g class="sector-dividers" stroke="var(--divider)" stroke-width="1.5">
        <line x1="242" y1="271" x2="342" y2="135"/>
        <line x1="283" y1="329" x2="444" y2="277"/>
        <line x1="283" y1="399" x2="444" y2="451"/>
        <line x1="242" y1="457" x2="342" y2="593"/>
      </g>
      <g class="inner-arcs">
        <path d="M173 191 A173 173 0 0 1 276 225 L241 272 A115 115 0 0 0 173 249Z" fill="var(--ink)"/>
        <path d="M276 225 A173 173 0 0 1 338 311 L282 329 A115 115 0 0 0 241 272Z" fill="var(--red)"/>
        <path d="M338 311 A173 173 0 0 1 338 417 L282 399 A115 115 0 0 0 282 329Z" fill="#a4a4a8"/>
        <path d="M338 417 A173 173 0 0 1 276 503 L241 456 A115 115 0 0 0 282 399Z" fill="var(--red)"/>
        <path d="M276 503 A173 173 0 0 1 173 537 L173 479 A115 115 0 0 0 241 456Z" fill="var(--ink)"/>
      </g>
    </g>

    <circle class="hub" cx="173" cy="364" r="115" fill="url(#hub-fill)"/>
    <circle class="hub-mark" cx="173" cy="364" r="86" fill="var(--ink)"/>

    <g class="value-icons">
      <rect x="210" y="117" width="58" height="58" rx="12" fill="#2a2a2a" opacity="0.85" role="img" aria-label="Teamwork icon: four hands joined in a circle"/>
      <rect x="330" y="202" width="58" height="58" rx="12" fill="var(--red)" role="img" aria-label="Family icon: house sheltering a group"/>
      <rect x="370" y="333" width="64" height="60" rx="12" fill="#2a2a2a" opacity="0.85" role="img" aria-label="Accountability icon: shield with tick and person"/>
      <rect x="331" y="470" width="66" height="64" rx="14" fill="var(--red)" role="img" aria-label="Honesty icon: heart with handshake"/>
      <g class="stars" fill="var(--ink)">
        <path d="M243 544l3.2 6.5 7.2 1-5.2 5.1 1.2 7.1-6.4-3.4-6.4 3.4 1.2-7.1-5.2-5.1 7.2-1z"/>
        <path d="M221 561l3.2 6.5 7.2 1-5.2 5.1 1.2 7.1-6.4-3.4-6.4 3.4 1.2-7.1-5.2-5.1 7.2-1z"/>
        <path d="M265 561l3.2 6.5 7.2 1-5.2 5.1 1.2 7.1-6.4-3.4-6.4 3.4 1.2-7.1-5.2-5.1 7.2-1z"/>
        <path d="M228 586l3.2 6.5 7.2 1-5.2 5.1 1.2 7.1-6.4-3.4-6.4 3.4 1.2-7.1-5.2-5.1 7.2-1z"/>
        <path d="M258 586l3.2 6.5 7.2 1-5.2 5.1 1.2 7.1-6.4-3.4-6.4 3.4 1.2-7.1-5.2-5.1 7.2-1z"/>
      </g>
    </g>
  </svg>

  <span class="brand-name">Brightwell</span>

  <h2 class="value-label" style="top:82px">TEAMWORK</h2>
  <h2 class="value-label" style="top:223px">FAMILY</h2>
  <h2 class="value-label" style="top:363px">ACCOUNTABILITY</h2>
  <h2 class="value-label" style="top:503px">HONESTY</h2>
  <h2 class="value-label" style="top:644px">EXCELLENCE</h2>

  <div class="behaviours" style="top:36px">
    <ul class="col-wide"><li>Acknowledge strengths and weaknesses</li><li>Compromise</li><li>Active Listening</li></ul>
    <ul><li>Punctuality</li><li>Mutual Respect</li><li>Open to Feedback</li></ul>
  </div>
  <div class="behaviours" style="top:182px">
    <ul class="col-wide"><li>Acceptance</li><li>Compassion</li></ul>
    <ul><li>Being there for<br>each other</li><li>Celebrating<br>Successes</li></ul>
  </div>
  <div class="behaviours" style="top:339px">
    <ul class="col-wide"><li>Responsibility</li><li>Trust</li></ul>
    <ul><li>Self-Discipline</li><li>Transparency</li></ul>
  </div>
  <div class="behaviours" style="top:478px">
    <ul class="col-mid"><li>Integrity</li><li>Vulnerability</li></ul>
    <ul style="width:92px"><li>Ethical</li><li>Truthful</li></ul>
    <ul><li>Psychological<br>Safety</li></ul>
  </div>
  <div class="behaviours" style="top:602px">
    <ul class="col-wide"><li>Service to others (Internally and Externally)</li><li>Consistent Quality</li><li>Continuous Improvement</li></ul>
    <ul><li>Attention to Detail</li><li>Accepting Challenges</li></ul>
  </div>
</main>
</body>
</html>
```